Construction Company Facebook Banner

We are a small residential building company, building mostly new homes, renovations, extensions. our social media needs an uplift to look more professional.
I have no photos I wish to use in the banner as of yet however I have included the company logo, and the business card design which has some details.
I would like something simple but professional.
The banner does not need to have email, phone number, services provided etc. all of this is available on the facebook page itself. Something simple and clean please.
Industry/Entity Type
Construction
Requirements
Should not have
- Images of people, QR Code

```html
<!DOCTYPE html>
<html lang="en">
<head>
<meta charset="utf-8">
<title>Tallowby Homes – Facebook Banner</title>
<link rel="stylesheet" href="https://fonts.googleapis.com/css2?family=Onest:wght@400;500;600&display=swap">
<style>
  :root {
    --brand-green: #2db34a;
    --ink: #1f1f1f;
    --muted: #7a7a7a;
    --haze: #f6f4f1;
    --sky: #cfe1f5;
    --sky-deep: #8fb7e2;
    --vest: #f08a3a;
  }
  * { margin: 0; padding: 0; box-sizing: border-box; }
  html, body {
    width: 1200px;
    height: 502px;
    overflow: hidden;
    background: #fff;
  }
  .banner {
    position: relative;
    width: 1200px;
    height: 502px;
    overflow: hidden;
    font-family: "Onest", sans-serif;
  }
  .site-backdrop {
    position: absolute;
    inset: 0;
    background:
      radial-gradient(ellipse at 18% 35%, #fffaf0 0%, rgba(255,250,240,0) 45%),
      linear-gradient(90deg, #ece8e3 0%, var(--haze) 35%, #f3f5f8 60%, #e8f0fa 100%);
  }
  .builder-photo {
    position: absolute;
    top: 0;
    right: 0;
    width: 520px;
    height: 502px;
    background:
      radial-gradient(ellipse at 62% 78%, rgba(240,138,58,0.55) 0%, rgba(240,138,58,0) 40%),
      linear-gradient(180deg, var(--sky-deep) 0%, var(--sky) 55%, #dfe6ee 100%);
    -webkit-mask-image: linear-gradient(90deg, transparent 0%, #000 35%);
            mask-image: linear-gradient(90deg, transparent 0%, #000 35%);
  }
  .brand {
    position: absolute;
    left: 32px;
    top: 68px;
    display: flex;
    align-items: flex-start;
    gap: 8px;
    color: var(--ink);
    font-weight: 600;
    line-height: 1;
  }
  .brand-square {
    width: 20px;
    height: 20px;
    margin-top: 2px;
    background: var(--brand-green);
  }
  .brand-name { display: block; font-size: 21px; letter-spacing: 0.2px; }
  .brand-sub { display: block; font-size: 8.5px; letter-spacing: 1.5px; margin-top: 4px; }
  .headline {
    position: absolute;
    left: 130px;
    top: 180px;
    color: var(--brand-green);
    font-weight: 600;
    font-size: 82px;
    line-height: 74px;
    letter-spacing: -1px;
  }
  .divider {
    position: absolute;
    left: 132px;
    top: 345px;
    width: 531px;
    height: 1px;
    background: var(--ink);
  }
  .services {
    position: absolute;
    left: 133px;
    top: 354px;
    color: var(--muted);
    font-weight: 400;
    font-size: 25px;
    letter-spacing: -0.2px;
  }
</style>
</head>
<body>
  <main class="banner">
    <div class="site-backdrop" role="img" aria-label="Faded photo of scaffolding on a construction site in bright sunlight"></div>
    <div class="builder-photo" role="img" aria-label="Photo of a builder in a blue hard hat and orange safety vest holding rolled plans in front of a building under construction"></div>

    <div class="brand">
      <span class="brand-square"></span>
      <div>
        <span class="brand-name">TALLOWBY HOMES</span>
        <span class="brand-sub">&amp; RENOVATIONS CO</span>
      </div>
    </div>

    <h1 class="headline">Building Quality<br>Homes for Life</h1>
    <div class="divider"></div>
    <p class="services">New Builds · Renovations · Extensions</p>
  </main>
</body>
</html>
```